Brantley Water Taxi and Transport

Need to redesign our business cards to relay that we do freight logistics and water taxi service. We also work with gov. agencies doing environmental clean up, oil spill response, remote site construction and work with many of the air taxi and helicopter services on Kodiak Island. Out website is www.brantleywatertaxi-example.com to get a better idea of what we do.

Contact Information for Business Card

I have a previous business card but it just has the logo on the front, and a sunset picture on the back with the contact info. It does not relay what we do and what we can help with. I like a simple straight forward design over a busy one.

Colors
3176b5
0455a3
cfdfed

Requirements
Must have
• logo, email, website, phone number

```html
<!DOCTYPE html>
<html lang="en">
<head>
<meta charset="utf-8">
<title>Brantley Water Taxi and Transport – Business Cards</title>
<link rel="stylesheet" href="https://fonts.googleapis.com/css2?family=Poppins:wght@400;500;600&display=swap">
<style>
  :root {
    --brand-blue: #0455a3;
    --mid-blue: #3176b5;
    --card-tint: #cfdfed;
    --card-light: #d8e5f1;
    --page-bg: #eef1f4;
    --ice-blue: #8fc4e6;
    --sun-orange: #f39a1e;
    --sand: #d9cdb3;
    --white: #ffffff;
  }
  * { box-sizing: border-box; margin: 0; padding: 0; }
  html, body {
    width: 1200px; height: 1200px; overflow: hidden;
    background: var(--page-bg);
    font-family: "Poppins", sans-serif;
  }
  .sheet {
    position: relative; width: 1200px; height: 1200px;
  }
  .card {
    position: absolute; left: 150px; width: 900px; height: 514px;
    background: linear-gradient(160deg, var(--card-light), var(--card-tint));
    box-shadow: 0 12px 30px rgba(0, 40, 90, 0.18);
    overflow: hidden;
  }
  .card--front { top: 56px; }
  .card--back { top: 630px; }

  /* Front */
  .front-frame {
    position: absolute; inset: 62px 110px;
    border: 3px solid var(--brand-blue);
  }
  .front-logo {
    position: absolute; left: 50%; top: 50%;
    transform: translate(-50%, -50%);
    display: flex; flex-direction: column; align-items: center; gap: 18px;
  }
  .logo-art {
    width: 300px; height: 150px; border-radius: 6px;
    background: linear-gradient(135deg, var(--ice-blue) 0%, #b9d6ea 55%, var(--sun-orange) 100%);
  }
  .brand-name {
    color: var(--brand-blue); font-weight: 600; font-size: 34px;
    letter-spacing: 0.5px; text-align: center; line-height: 1.2;
  }

  /* Back */
  .contact-band {
    position: absolute; left: 0; top: 40px; width: 330px; height: 46px;
    background: var(--brand-blue);
    display: flex; align-items: center; justify-content: flex-end;
    padding-right: 22px;
  }
  .contact-band__label {
    color: var(--white); font-weight: 500; font-size: 22px; letter-spacing: 0.5px;
  }
  .contact-list {
    position: absolute; left: 56px; top: 130px;
    list-style: none; display: flex; flex-direction: column; gap: 20px;
  }
  .contact-item {
    display: flex; align-items: center; gap: 18px;
    color: var(--brand-blue); font-size: 20px;
  }
  .contact-item svg { width: 30px; height: 30px; flex: none; }
  .back-art {
    position: absolute; left: 120px; right: 60px; bottom: 0; height: 200px;
    background: linear-gradient(90deg, rgba(143,196,230,0.25), rgba(143,196,230,0.45) 60%, rgba(217,205,179,0.7));
    border-radius: 10px 10px 0 0;
  }
  .back-logo {
    position: absolute; right: 56px; top: 170px; width: 300px;
    text-align: right;
  }
  .back-logo .brand-name { font-size: 28px; text-align: right; }
</style>
</head>
<body>
<main class="sheet">

  <section class="card card--front" aria-label="Business card front">
    <div class="front-frame"></div>
    <div class="front-logo">
      <div class="logo-art" role="img" aria-label="Illustration of a workboat in front of icy mountains and a setting sun"></div>
      <p class="brand-name">Brantley Water Taxi &amp; Transport</p>
    </div>
  </section>

  <section class="card card--back" aria-label="Business card back">
    <div class="back-art" role="img" aria-label="Faint illustration of a workboat, waves, mountains and sun"></div>
    <div class="contact-band"><span class="contact-band__label">CONTACT US</span></div>
    <ul class="contact-list">
      <li class="contact-item">
        <svg viewBox="0 0 30 30" aria-hidden="true"><circle cx="15" cy="15" r="14" fill="var(--brand-blue)"/><path d="M10 8c1-1 2 0 3 2s0 2-1 3c1 2 2 3 4 4 1-1 2-2 3-1s3 2 2 3-2 2-4 1c-4-1-8-5-9-9 0-1 1-2 2-3z" fill="var(--white)"/></svg>
        <span>555-014-2200</span>
      </li>
      <li class="contact-item">
        <svg viewBox="0 0 30 30" aria-hidden="true"><circle cx="15" cy="15" r="14" fill="var(--brand-blue)"/><rect x="8" y="10" width="14" height="10" fill="none" stroke="var(--white)" stroke-width="1.8"/><path d="M8 10l7 6 7-6" fill="none" stroke="var(--white)" stroke-width="1.8"/></svg>
        <span>brantleywatertaxi@example.com</span>
      </li>
      <li class="contact-item">
        <svg viewBox="0 0 30 30" aria-hidden="true"><circle cx="15" cy="15" r="14" fill="var(--brand-blue)"/><circle cx="15" cy="15" r="8" fill="none" stroke="var(--white)" stroke-width="1.5"/><ellipse cx="15" cy="15" rx="3.5" ry="8" fill="none" stroke="var(--white)" stroke-width="1.5"/><path d="M7 15h16" stroke="var(--white)" stroke-width="1.5"/></svg>
        <span>www.brantleywatertaxi-example.com</span>
      </li>
      <li class="contact-item">
        <svg viewBox="0 0 30 30" aria-hidden="true"><circle cx="15" cy="15" r="14" fill="var(--brand-blue)"/><path d="M26 22l3 5-6-2z" fill="var(--brand-blue)"/></svg>
        <span>Call us for a free quote today</span>
      </li>
    </ul>
    <div class="back-logo">
      <p class="brand-name">Brantley Water Taxi &amp; Transport</p>
    </div>
  </section>

</main>
</body>
</html>
```